Business Card Design needed Have Logo Files

Hello, I am in need of a business card design.

Company Name: Quartz Traders

Company Address:
2714 E. Palmer Ave
Suite 482B
North Las Vegas, Nevada 97415

I think the colors blue, grey, silver (metallic), white, and black are good choices to go with for coloring.

The Owen Pratt and the Copper Sheet are my favorites from the examples so far. Love the bring and edgy blues.

Photo's I have added are designs that I like. I'll also be adding source files.

Logo Source documents have been added.

Project Deadline Extended
Reason: Father passed away and had to take care of his affairs, back in business now.

Need front and back. Try to give it a backside that has a wow factor to it. I've changed the color spectrum to blue, black, purple, and pink for the front side. Think of it as 90% blue and black, 7% purple, 3 % pink when it comes to thinking of ratios of how much of each color i'd like to see on the card. Backside you can use any of those 4 colors as much as you'd like to give it memorable.

Industry/Entity Type

Business

Colors
0492cd
33a6d7
0355a3
3176b5
ffffff
aaaaaa
cbcbcb
9d9d9d
5c5c5c

Requirements
Must have
• Name
Company Address
Work Number
Mobile Number

Doublesided.
Rounded edges

```html
<!DOCTYPE html>
<html lang="en">
<head>
<meta charset="utf-8">
<title>Quartz Traders — Business Card</title>
<link rel="stylesheet" href="https://fonts.googleapis.com/css2?family=Arimo:wght@400;700&display=swap">
<style>
  :root {
    --ink-black: #000000;
    --board-dark: #050505;
    --board-glow: #4a4a4a;
    --card-black: #000000;
    --white: #ffffff;
    --silver: #cbcbcb;
    --smoke-blue: #0492cd;
    --smoke-deep: #0355a3;
    --smoke-light: #33a6d7;
    --accent-purple: #6a2bb8;
    --accent-pink: #e0409a;
  }
  * { margin: 0; padding: 0; box-sizing: border-box; }
  html, body {
    width: 1200px;
    height: 1000px;
    overflow: hidden;
    background: var(--ink-black);
  }
  .board {
    position: relative;
    width: 1200px;
    height: 1000px;
    overflow: hidden;
    background: radial-gradient(ellipse 900px 700px at 1000px 820px, var(--board-glow) 0%, #262626 40%, var(--board-dark) 85%);
    font-family: "Arimo", Arial, sans-serif;
    color: var(--white);
  }
  .brand-mark {
    position: absolute;
    left: 62px;
    top: 82px;
    display: flex;
    align-items: center;
    gap: 54px;
  }
  .brand-mark__dot {
    width: 80px;
    height: 80px;
    border-radius: 50%;
    background: var(--white);
  }
  .brand-mark__name {
    font-weight: 700;
    font-size: 66px;
    letter-spacing: 8px;
    line-height: 1;
    color: var(--white);
  }
  .card {
    position: absolute;
    top: 616px;
    width: 371px;
    height: 217px;
    border-radius: 14px;
    background: var(--card-black);
    overflow: hidden;
  }
  .card--front { left: 363px; }
  .card--back {
    left: 756px;
    display: flex;
    align-items: center;
    justify-content: center;
  }
  .card__smoke {
    position: absolute;
    inset: 0;
    background:
      radial-gradient(ellipse 140px 60px at 230px 30px, rgba(51,166,215,0.75), transparent 70%),
      radial-gradient(ellipse 120px 90px at 330px 110px, rgba(4,146,205,0.55), transparent 70%),
      radial-gradient(ellipse 110px 50px at 130px 80px, rgba(3,85,163,0.6), transparent 70%),
      radial-gradient(ellipse 90px 40px at 60px 20px, rgba(4,146,205,0.35), transparent 70%),
      radial-gradient(ellipse 60px 30px at 300px 190px, rgba(106,43,184,0.35), transparent 70%);
  }
  .card__logo {
    position: absolute;
    left: 17px;
    top: 34px;
    display: flex;
    align-items: center;
    gap: 12px;
  }
  .card__logo-dot {
    width: 26px;
    height: 26px;
    border-radius: 50%;
    background: var(--white);
  }
  .card__logo-name {
    font-weight: 700;
    font-size: 25px;
    letter-spacing: 3px;
    line-height: 1;
    color: var(--white);
  }
  .card__details {
    position: absolute;
    left: 24px;
    top: 100px;
    font-size: 11.5px;
    line-height: 15.5px;
    color: var(--white);
  }
  .card__company { margin-bottom: 15.5px; }
  .card__phones {
    position: absolute;
    right: 20px;
    bottom: 26px;
    font-size: 11.5px;
    line-height: 15.5px;
    text-align: right;
    color: var(--white);
  }
  .card__back-glow {
    position: absolute;
    inset: 0;
    background:
      radial-gradient(ellipse 170px 90px at 185px 108px, rgba(4,146,205,0.55), transparent 70%),
      radial-gradient(ellipse 120px 70px at 90px 170px, rgba(106,43,184,0.45), transparent 70%),
      radial-gradient(ellipse 90px 50px at 300px 40px, rgba(224,64,154,0.35), transparent 70%);
  }
  .card__back-ring {
    position: absolute;
    left: 50%;
    top: 50%;
    width: 230px;
    height: 230px;
    margin: -115px 0 0 -115px;
    border-radius: 50%;
    border: 1.5px solid rgba(51,166,215,0.45);
  }
  .card__back-name {
    position: relative;
    font-weight: 700;
    font-size: 48px;
    letter-spacing: 5px;
    color: var(--white);
  }
</style>
</head>
<body>
<main class="board">
  <div class="brand-mark">
    <span class="brand-mark__dot"></span>
    <span class="brand-mark__name">QUARTZ</span>
  </div>

  <section class="card card--front">
    <div class="card__smoke" role="img" aria-label="Wisps of glowing blue smoke across the black card"></div>
    <div class="card__logo">
      <span class="card__logo-dot"></span>
      <span class="card__logo-name">QUARTZ</span>
    </div>
    <div class="card__details">
      <p class="card__company">Quartz Traders</p>
      <p>Address:</p>
      <p>2714 E. Palmer Ave</p>
      <p>Suite 482B</p>
      <p>North Las Vegas, Nevada 97415</p>
    </div>
    <div class="card__phones">
      <p>Work: (702) 555-0148</p>
      <p>Mobile: (702) 555-0193</p>
    </div>
  </section>

  <section class="card card--back">
    <div class="card__back-glow"></div>
    <div class="card__back-ring"></div>
    <span class="card__back-name">QUARTZ</span>
  </section>
</main>
</body>
</html>
```